Small boutique multi-family apartment developer needs premium website design.

We are a growing real estate development company specializing in multi family apartment development. Our company Brindel Asset Development focuses on passive real estate investors looking to maximize their current real estate portfolio by allowing us to develop and reposition their current properties allowing them more cashflow while we are also able to take over the management of their asset in order to ensure optimal performance on a consistent basis.

```html
<!DOCTYPE html>
<html lang="en">
<head>
<meta charset="utf-8">
<title>Brindel Asset Development</title>
<link href="https://fonts.googleapis.com/css2?family=Cormorant+Garamond:wght@500;600&family=Outfit:wght@400;500;600&display=swap" rel="stylesheet">
<style>
:root{
  --navy:#142c7e;
  --navy-deep:#10246b;
  --ink:#1b1b1b;
  --muted:#333;
  --field:#e6e6e6;
  --white:#fff;
  --sea:#6fd0e3;
}
*{box-sizing:border-box;margin:0;padding:0}
html,body{width:1200px;height:3922px;overflow:hidden}
body{position:relative;font-family:'Outfit',sans-serif;color:var(--ink);background:var(--white)}
.abs{position:absolute}
.serif{font-family:'Cormorant Garamond',serif;font-weight:600}
.photo{position:absolute}

/* hero */
.hero{left:0;top:0;width:1200px;height:640px;background:linear-gradient(100deg,#2a2f33 0%,#4c5559 45%,#7d8a86 70%,#6e8464 100%)}
.hero-shade{left:0;top:0;width:1200px;height:640px;background:linear-gradient(90deg,rgba(10,15,25,.55),rgba(10,15,25,.1))}
.brand{display:flex;align-items:center;gap:16px}
.brand-mark{width:50px;height:50px;background:var(--white)}
.brand-name{font-weight:500;font-size:22px;line-height:1.15;color:var(--white)}
.nav{top:44px;right:0;display:flex;gap:36px;left:594px;font-size:15px;font-weight:500;color:var(--white)}
.nav-contact{left:1039px;top:37px;width:97px;height:36px;background:var(--white);color:var(--navy);font-weight:600;font-size:15px;display:flex;align-items:center;justify-content:center}
.hero-title{left:62px;top:176px;font-size:50px;line-height:56px;color:var(--white)}
.hero-text{left:62px;top:326px;width:390px;font-size:13px;line-height:27px;color:var(--white)}
.btn{display:flex;align-items:center;justify-content:center;font-size:14px;font-weight:500;color:var(--white)}
.btn-solid{background:var(--navy)}
.btn-ghost{border:1.5px solid var(--white)}

/* about */
.section-title{font-size:40px;color:var(--ink)}
.body-text{font-size:12.5px;line-height:21px;color:var(--muted)}

/* properties */
.card-featured{left:62px;top:1214px;width:279px;height:349px;background:var(--navy)}
.price{font-size:15px;font-weight:600}
.prop-name{font-size:18px;font-weight:600}
.arrow{width:40px;height:40px;border-radius:50%;display:flex;align-items:center;justify-content:center}

/* lifestyle */
.lifestyle{left:0;top:1652px;width:1200px;height:1059px;background:var(--navy)}
.tile-label{width:340px;text-align:center;font-size:19px;font-weight:600;color:var(--white)}

/* contact */
.field{background:var(--field);font-size:12px;color:#888;padding-left:16px;display:flex;align-items:center}
.contact-row{display:flex;align-items:center;gap:20px;font-size:13px;line-height:14px}
.icon{width:34px;height:34px;border-radius:50%;background:var(--ink);display:flex;align-items:center;justify-content:center;flex:none}

/* footer */
.foot-title{font-size:24px;color:var(--navy)}
.foot-list{list-style:none;font-size:14px}
.foot-list li::before{content:"•";margin-right:10px}
.social{width:30px;height:30px;border-radius:50%;background:var(--navy)}
.bottom-bar{left:0;top:3877px;width:1200px;height:45px;background:var(--navy);color:var(--white);font-size:15px;display:flex;align-items:center;justify-content:center;gap:36px}
</style>
</head>
<body>

<!-- Hero -->
<div class="abs hero" role="img" aria-label="Modern multi-storey apartment buildings with a paved walkway and lawns"></div>
<div class="abs hero-shade"></div>
<div class="abs brand" style="left:66px;top:30px">
  <div class="brand-mark"></div>
  <div class="brand-name">Brindel Asset<br>Development</div>
</div>
<nav class="abs nav">
  <span>Home</span><span>About Us</span><span>Our Properties</span><span>Lifestyle</span>
</nav>
<div class="abs nav-contact">Contact</div>
<h1 class="abs serif hero-title">Elevate Your Lifestyle with<br>Our Premium Apartments</h1>
<p class="abs hero-text">Lorem ipsum dolor sit amet, consectetuer adipiscing elit, sed diam nonummy nibh euismod tincidunt ut laoreet dolore magna aliquam erat volutpat. Ut wisi enim ad minim veniam, quis nostrud exerci tation ullamcorper suscipit lobortis nisl ut aliquip</p>
<div class="abs btn btn-solid" style="left:62px;top:510px;width:148px;height:34px">Read more</div>
<div class="abs btn btn-ghost" style="left:227px;top:510px;width:148px;height:34px">Contact us</div>

<!-- About -->
<div class="photo" style="left:62px;top:699px;width:491px;height:286px;background:linear-gradient(180deg,#5d8fcf 0%,#c9d6e4 45%,#d9d7cf 70%,#4f8a3a 100%)" role="img" aria-label="Modern white apartment block under a blue sky with green lawn"></div>
<h2 class="abs serif section-title" style="left:623px;top:710px">About Us</h2>
<p class="abs body-text" style="left:623px;top:775px;width:510px">Lorem ipsum dolor sit amet, consectetuer adipiscing elit, sed diam nonummy nibh euismod tincidunt ut laoreet dolore magna aliquam erat volutpat. Ut wisi enim ad minim veniam, quis nostrud exerci tation ullamcorper suscipit lobortis nisl ut aliquip Lorem ipsum dolor sit amet, consectetuer adipiscing elit, sed diam nonummy nibh euismod tincidunt Lorem ipsum dolor sit amet, consectetuer adipiscing elit, sed diam nonummy nibh euismod tincidunt ut laoreet dolore magna aliquam erat volutpat. Ut wisi enim ad minim veniam, quis nostrud</p>
<div class="abs btn btn-solid" style="left:623px;top:950px;width:148px;height:35px">Read more</div>

<!-- Properties -->
<h2 class="abs serif section-title" style="left:0;width:1224px;text-align:center;top:1068px">Our Properties</h2>
<p class="abs body-text" style="left:190px;width:843px;text-align:center;top:1128px">Lorem ipsum dolor sit amet, consectetuer adipiscing elit, sed diam nonummy nibh euismod tincidunt ut laoreet dolore magna aliquam erat volutpat. Ut wisi enim ad minim veniam, quis nostrud exerci tation ullamcorper suscipit lobortis nisl ut aliquip Lorem ipsum dolor sit amet,</p>

<div class="abs card-featured"></div>
<div class="photo" style="left:79px;top:1231px;width:245px;height:243px;background:linear-gradient(180deg,#b9c9dc 0%,#d7d2c9 50%,#b5683f 75%,#4a7a3c 100%)" role="img" aria-label="Brick and white apartment buildings along a garden path"></div>
<div class="abs price" style="left:79px;top:1490px;color:var(--white)">500$</div>
<div class="abs prop-name" style="left:79px;top:1523px;color:var(--white)">Sunshine Apartments</div>
<div class="abs arrow" style="left:277px;top:1505px;background:var(--white)">
  <svg width="16" height="16" viewBox="0 0 16 16"><path d="M4 12L12 4M6 4h6v6" fill="none" stroke="#142c7e" stroke-width="1.6"/></svg>
</div>

<div class="photo" style="left:372px;top:1221px;width:245px;height:255px;background:linear-gradient(180deg,#efe9e0 0%,#d9c8b0 55%,#a98a66 100%)" role="img" aria-label="Bright living and dining room interior"></div>
<div class="abs price" style="left:372px;top:1498px;color:var(--navy)">654$</div>
<div class="abs prop-name" style="left:372px;top:1534px">Silver House</div>
<div class="abs arrow" style="left:570px;top:1506px;background:var(--navy)">
  <svg width="16" height="16" viewBox="0 0 16 16"><path d="M4 4l8 8M12 6v6H6" fill="none" stroke="#fff" stroke-width="1.6"/></svg>
</div>

<div class="photo" style="left:632px;top:1221px;width:245px;height:255px;background:linear-gradient(180deg,#4b5a7a 0%,#8a8070 50%,#c7a27a 100%)" role="img" aria-label="Living room with large windows over a city at dusk"></div>
<div class="abs price" style="left:632px;top:1498px;color:var(--navy)">473$</div>
<div class="abs prop-name" style="left:632px;top:1534px">Jolly City</div>
<div class="abs arrow" style="left:830px;top:1506px;background:var(--navy)">
  <svg width="16" height="16" viewBox="0 0 16 16"><path d="M4 4l8 8M12 6v6H6" fill="none" stroke="#fff" stroke-width="1.6"/></svg>
</div>

<div class="photo" style="left:892px;top:1221px;width:246px;height:255px;background:linear-gradient(180deg,#8fb6e0 0%,#e4e2dc 50%,#c9b39a 75%,#5f8f44 100%)" role="img" aria-label="White apartment building with balconies and lawn"></div>
<div class="abs price" style="left:892px;top:1498px;color:var(--navy)">832$</div>
<div class="abs prop-name" style="left:892px;top:1534px">Greenhouse</div>
<div class="abs arrow" style="left:1095px;top:1506px;background:var(--navy)">
  <svg width="16" height="16" viewBox="0 0 16 16"><path d="M4 4l8 8M12 6v6H6" fill="none" stroke="#fff" stroke-width="1.6"/></svg>
</div>

<!-- Lifestyle -->
<div class="abs lifestyle"></div>
<h2 class="abs serif section-title" style="left:0;width:1212px;text-align:center;top:1678px;color:var(--white)">Lifestyle</h2>
<p class="abs body-text" style="left:170px;width:880px;text-align:center;top:1745px;color:var(--white)">Lorem ipsum dolor sit amet, consectetuer adipiscing elit, sed diam nonummy nibh euismod tincidunt ut laoreet dolore magna aliquam erat volutpat. Ut wisi enim ad minim veniam, quis nostrud exerci tation ullamcorper suscipit lobortis nisl ut aliquip Lorem ipsum dolor sit amet, conse</p>

<div class="photo" style="left:65px;top:1823px;width:340px;height:340px;background:linear-gradient(180deg,#6e95c4 0%,#b9a58a 55%,#3f5a35 100%)" role="img" aria-label="Luxury villa-style apartments with terraces"></div>
<div class="photo" style="left:429px;top:1823px;width:340px;height:340px;background:linear-gradient(180deg,#d8d4cc 0%,#9aa39a 50%,#a5754a 100%)" role="img" aria-label="Fitness center with gym equipment"></div>
<div class="photo" style="left:795px;top:1823px;width:340px;height:340px;background:linear-gradient(180deg,#9fd3e6 0%,#2fb0c9 45%,#3e8d3e 65%,#1f8fd0 100%)" role="img" aria-label="Resort pool surrounded by palm trees"></div>
<div class="abs tile-label" style="left:65px;top:2189px">Luxury Apartments</div>
<div class="abs tile-label" style="left:438px;top:2189px">Fitness Center</div>
<div class="abs tile-label" style="left:797px;top:2189px">Pool</div>

<div class="photo" style="left:65px;top:2277px;width:340px;height:340px;background:linear-gradient(135deg,#eef3f7 0%,#c9dbe8 55%,#eacfd8 100%)" role="img" aria-label="Hospitality care scene"></div>
<div class="photo" style="left:429px;top:2277px;width:340px;height:340px;background:radial-gradient(circle,#ffffff 0%,#f4efe9 40%,#a97f62 75%,#5b3d2c 100%)" role="img" aria-label="Group of hands joined in a circle for community events"></div>
<div class="photo" style="left:795px;top:2277px;width:340px;height:340px;background:linear-gradient(180deg,#6d7f95 0%,#8a8a86 45%,#c7512a 75%,#3d3430 100%)" role="img" aria-label="Rooftop terrace lounge overlooking the city"></div>
<div class="abs tile-label" style="left:70px;top:2641px">Hospitality</div>
<div class="abs tile-label" style="left:434px;top:2641px">Events</div>
<div class="abs tile-label" style="left:805px;top:2641px">Rooftop Terrace</div>

<!-- Contact -->
<h2 class="abs serif section-title" style="left:64px;top:2754px">Contact</h2>
<h2 class="abs serif section-title" style="left:530px;width:606px;text-align:center;top:2762px">How We Can Help You ?</h2>
<div class="abs" style="left:59px;top:2836px;font-size:32px;line-height:44px;font-weight:500;color:var(--navy)">Get in Touch for<br>Exclusive Offers</div>

<div class="abs contact-row" style="left:62px;top:2971px">
  <div class="icon"><svg width="16" height="16" viewBox="0 0 24 24"><path d="M6.6 10.8a15 15 0 006.6 6.6l2.2-2.2a1 1 0 011-.25 11.4 11.4 0 003.6.57 1 1 0 011 1V20a1 1 0 01-1 1A17 17 0 013 4a1 1 0 011-1h3.5a1 1 0 011 1c0 1.25.2 2.45.57 3.57a1 1 0 01-.25 1z" fill="#fff"/></svg></div>
  <span>0100 555 0199</span>
</div>
<div class="abs contact-row" style="left:62px;top:3031px">
  <div class="icon"><svg width="16" height="18" viewBox="0 0 24 24"><path d="M12 2a7 7 0 00-7 7c0 5 7 13 7 13s7-8 7-13a7 7 0 00-7-7zm0 9.5A2.5 2.5 0 1112 6.5a2.5 2.5 0 010 5z" fill="#fff"/></svg></div>
  <span>14 Harbor Crest Avenue,<br>Marlow Bay</span>
</div>
<div class="abs contact-row" style="left:62px;top:3092px">
  <div class="icon"><svg width="18" height="18" viewBox="0 0 24 24" fill="none" stroke="#fff" stroke-width="1.6"><circle cx="12" cy="12" r="9"/><path d="M3 12h18M12 3c3 3 3 15 0 18M12 3c-3 3-3 15 0 18"/></svg></div>
  <span>www.brindelasset.com</span>
</div>

<div class="abs field" style="left:530px;top:2834px;width:294px;height:37px">Your Name</div>
<div class="abs field" style="left:841px;top:2834px;width:295px;height:37px">E Mail</div>
<div class="abs field" style="left:530px;top:2886px;width:294px;height:35px">Phone .No</div>
<div class="abs field" style="left:841px;top:2886px;width:295px;height:35px">Apartment</div>
<div class="abs field" style="left:530px;top:2944px;width:606px;height:116px;align-items:flex-start;padding-top:14px;font-size:14px">Message...</div>
<div class="abs btn" style="left:530px;top:3084px;width:606px;height:41px;background:#000;font-size:15px;font-weight:600">Submit</div>

<!-- Map -->
<div class="photo" style="left:62px;top:3198px;width:1074px;height:351px;background:linear-gradient(90deg,var(--sea) 0%,#dfe8d4 20%,#eee9d8 55%,#dfe8d4 85%,var(--sea) 100%)" role="img" aria-label="Map of property locations across North America"></div>
<div class="abs" style="left:87px;top:3224px;font-size:16px;color:var(--white)">Property Locations</div>

<!-- Footer -->
<div class="abs brand" style="left:64px;top:3615px">
  <div class="brand-mark" style="background:var(--navy)"></div>
  <div class="brand-name" style="color:var(--navy)">Brindel Asset<br>Development</div>
</div>
<p class="abs" style="left:64px;top:3703px;width:290px;font-size:14px;line-height:21px">Lorem ipsum dolor sit amet, consectetuer adipiscing elit, sed diam nonummy nibh Lorem ipsum dolor sit amet, consectetuer</p>
<div class="abs social" style="left:66px;top:3793px"></div>
<div class="abs social" style="left:113px;top:3793px"></div>
<div class="abs social" style="left:162px;top:3793px"></div>

<h3 class="abs serif foot-title" style="left:470px;top:3610px">Quick link</h3>
<ul class="abs foot-list" style="left:474px;top:3658px;line-height:37px">
  <li>Home</li><li>About Us</li><li>Our Properties</li><li>Lifestyle</li><li>Contact</li>
</ul>
<h3 class="abs serif foot-title" style="left:704px;top:3608px">Our Properties</h3>
<ul class="abs foot-list" style="left:704px;top:3655px;line-height:38px">
  <li>Luxury Apartments</li><li>Green House</li><li>Silver House</li><li>Jolly City</li><li>Greenhouse</li>
</ul>
<h3 class="abs serif foot-title" style="left:953px;top:3610px">News Letter</h3>
<p class="abs" style="left:953px;top:3663px;font-size:14px;line-height:15px">Subscribe For News Letter<br>and events</p>
<div class="abs" style="left:953px;top:3728px;width:145px;height:30px;border:1px solid #999;font-size:12px;color:#888;padding-left:10px;display:flex;align-items:center">Enter your mail</div>
<div class="abs" style="left:1098px;top:3728px;width:40px;height:30px;background:var(--navy);display:flex;align-items:center;justify-content:center">
  <svg width="22" height="10" viewBox="0 0 22 10"><path d="M1 5h19M15 1l4 4-4 4" fill="none" stroke="#fff" stroke-width="1.5"/></svg>
</div>

<div class="abs bottom-bar">
  <span>© Copyright 2024&nbsp; All Rights Reserved.</span>
  <span>Privacy policy</span>
  <span style="border-left:1.5px solid #fff;padding-left:24px">Terms &amp; Conditions</span>
</div>

</body>
</html>
```